New College Graduate Resume - Creative and unique design that stands out from the rest

Need creative resume design for recent college graduate who graduated from School of Music with a concentration in music composition and production. Striving for a contemporary layout/design that allows the resume to "be unique" and "stand out" but be polished and professional. Open to integrating moderate color/graphics as part of resume design but the design can be minus those attributes as well. Attached is raw content in 7 sections (name/contact info, education, highlights of qualifications, work experience, honors/awards, and professional affiliations). While the designer has full latitude over overall design which (section headers, font type, separation/spacing, use of bullets, justification of text, etc.) please maintain current order/sequence of the 7 sections.

Industry/Entity Type

School

Requirements
Must have
• Name (Tobias Hale Whitcombe II) should be most prominent (bold/font size) compared to remainder of resume copy.
• Section headers should be prominent but less so when compared to name on resume.
• The attached file of resume content is provided as raw source copy and is NOT to be just copied and pasted into open fields as is. Expectation is each section of copy will be organized in a manner that is most visually appealing and may include bullets, appropriate spacing, etc.
Should not have
• The attached file of resume content is provided as source copy and is NOT to be just copied and pasted into open fields as is. Expectation is each section of copy will be organized in a manner that

```html
<!DOCTYPE html>
<html lang="en">
<head>
<meta charset="utf-8">
<title>Tobias Hale Whitcombe II – Resume, Page 2</title>
<link href="https://fonts.googleapis.com/css2?family=Roboto+Condensed:wght@400;700&family=Roboto:wght@400&display=swap" rel="stylesheet">
<style>
  :root {
    --navy-deep: #0a0a48;
    --navy-glow: #2a3088;
    --ink-navy: #2b2a6c;
    --accent-red: #b51d24;
    --accent-red-dark: #6e1014;
    --paper: #ffffff;
    --body-ink: #1c1c1c;
    --side-ink: #e6e8f4;
  }
  * { margin: 0; padding: 0; box-sizing: border-box; }
  html, body { width: 927px; height: 1200px; overflow: hidden; }
  body {
    position: relative;
    background: radial-gradient(ellipse 420px 620px at 700px 560px, var(--navy-glow) 0%, #161a66 45%, var(--navy-deep) 100%);
    font-family: "Roboto", Arial, sans-serif;
  }
  .main-column {
    position: absolute; left: 77px; top: 0; width: 514px; height: 1098px;
    background: var(--paper);
  }
  .section-banner {
    position: absolute; left: 55px; top: 82px; width: 508px; height: 49px;
    background: var(--accent-red);
    box-shadow: 3px 4px 6px rgba(0,0,0,0.35);
    color: var(--paper);
    font-family: "Roboto Condensed", Arial, sans-serif; font-weight: 700;
    font-size: 26px; line-height: 49px; padding-left: 68px; letter-spacing: 0.2px;
  }
  .banner-fold { position: absolute; left: 55px; top: 131px; }
  .job { position: absolute; left: 123px; width: 440px; }
  .job-org, .job-place, .job-dates {
    font-family: "Roboto Condensed", Arial, sans-serif; font-weight: 700;
    color: var(--ink-navy); font-size: 16.5px; line-height: 22px;
  }
  .job-title {
    font-family: "Roboto Condensed", Arial, sans-serif; font-weight: 700;
    color: var(--accent-red); font-size: 16.5px; line-height: 22px; margin-top: 4px;
  }
  .bullets { list-style: none; margin-top: 4px; }
  .bullets li {
    font-size: 16.2px; line-height: 21.8px; color: var(--body-ink); margin-bottom: 5px;
  }
  .bullets li::before {
    content: ""; display: inline-block; width: 0; height: 0;
    border-top: 5px solid transparent; border-bottom: 5px solid transparent;
    border-left: 6px solid var(--accent-red); margin-right: 5px; vertical-align: 0;
  }
  .side-section { position: absolute; left: 628px; width: 240px; }
  .side-heading {
    font-family: "Roboto Condensed", Arial, sans-serif; font-weight: 700;
    color: var(--accent-red); font-size: 27px; line-height: 34px; margin-bottom: 16px;
  }
  .side-section .bullets li { color: var(--side-ink); margin-bottom: 9px; }
</style>
</head>
<body>
  <div class="main-column"></div>
  <svg class="banner-fold" width="22" height="7" viewBox="0 0 22 7"><polygon points="0,0 22,0 22,7" fill="var(--accent-red-dark)"/></svg>
  <h2 class="section-banner">WORK EXPERIENCE</h2>

  <section class="job" style="top:150px">
    <div class="job-org">Coral Reel Studios (CRS)</div>
    <div class="job-place">Miami, FL</div>
    <div class="job-dates">May 2014 – Present</div>
    <div class="job-title">Sound Engineer</div>
    <ul class="bullets">
      <li>Edited and mixed recorded field audio to professional standards.</li>
      <li>Matched audio with motion picture video to create a seamless product.</li>
      <li>Recorded automated dialogue replacement (ADR) audio and integrated into motion picture video project using TrackForge 11.</li>
      <li>Recorded foley sound effects to be added to film, video, and other media in post-production.</li>
      <li>Composed and recorded original music to accompany various video projects.</li>
    </ul>
  </section>

  <section class="job" style="top:524px">
    <div class="job-org">Brightcart Stores</div>
    <div class="job-place">Atlanta, GA</div>
    <div class="job-dates">May 2013 - October 2013</div>
    <div class="job-title">Sales Associate</div>
    <ul class="bullets">
      <li>Provided customer service, maintained a clean and organized work environment, assisted in sales, and performed cashier responsibilities.</li>
    </ul>
  </section>

  <section class="job" style="top:707px">
    <div class="job-org">Peachtree Civic Action Network (PCAN)</div>
    <div class="job-place">Atlanta, GA</div>
    <div class="job-dates">June 2012 - August 2012</div>
    <div class="job-title">On-Site Promoter/Intern</div>
    <ul class="bullets">
      <li>Promoted and advertised various campaigns and managed various office tasks, such as setting up site maps and organizing and sorting non-profit donations.</li>
    </ul>
  </section>

  <section class="job" style="top:890px">
    <div class="job-org">Northline Direct, Incorporated</div>
    <div class="job-place">Atlanta, GA</div>
    <div class="job-dates">June 2011 – August 2011</div>
    <div class="job-title">Product Marketing Consultant</div>
    <ul class="bullets">
      <li>Conducted direct sales and marketing of subsidiary product line through establishing a compelling value proposition, overcoming objections, and closing the sale.</li>
    </ul>
  </section>

  <section class="side-section" style="top:357px">
    <h2 class="side-heading">HONORS/AWARDS</h2>
    <ul class="bullets">
      <li>Best Film and Score: Frights and Fanfares 2015 Competition (Bayview University)</li>
      <li>Edwin L Marsh Scholar</li>
      <li>Best New Member, Delta Tau Omega Fraternity, Inc.</li>
      <li>Bayview University Homecoming King, 2012</li>
    </ul>
  </section>

  <section class="side-section" style="top:700px">
    <h2 class="side-heading">PROFESSIONAL AFFILIATIONS</h2>
    <ul class="bullets">
      <li>Member, Guild of Contemporary Composers (GCC)</li>
      <li>Member, National Alliance of Composers, Authors, and Publishers (NACAP)</li>
      <li>Member, Sound Engineering Collective (SEC)</li>
      <li>Member, Delta Tau Omega Fraternity, Incorporated</li>
    </ul>
  </section>
</body>
</html>
```